Brightgate Business Card Design

Name Marisa Okonduye
Title Mortgage Originator
Office (800) 555-0142 x65
Direct (240) 555-0187
Email mokonduye@brightgatehomes.example
NMLS 5830472
Licensed MD

Name Deron Plummer
Title Mortgage Originator
Office (800) 555-0142 x66
Direct (404) 555-0163
Email dplummer@brightgatehomes.example
NMLS 5917360
Licensed MD

Name Lakendra Burton
Title Mortgage Originator
Office (800) 555-0142 x67
Direct (443) 555-0129
Email burtonlakendra@mailbox.example
NMLS 5372619
Licensed MD

Name Samir Qudwaheli
Title Mortgage Originator
Office (800) 555-0142 x32
Direct (571) 555-0176
Email squdwaheli@brightgatehomes.example
NMLS 4068259
Licensed MD

```html
<!DOCTYPE html>
<html lang="en">
<head>
<meta charset="utf-8">
<title>Brightgate Business Card Design</title>
<link href="https://fonts.googleapis.com/css2?family=Lato:wght@400;700&display=swap" rel="stylesheet">
<style>
  :root {
    --backdrop: #d3d5d8;
    --card: #ffffff;
    --ink: #333437;
    --ink-soft: #3c3d40;
    --rule: #4a4b4e;
    --frame: #333333;
  }
  * { margin: 0; padding: 0; box-sizing: border-box; }
  html, body { width: 748px; height: 1200px; overflow: hidden; }
  body {
    background: var(--backdrop);
    font-family: "Lato", sans-serif;
    color: var(--ink);
    position: relative;
  }
  .card {
    position: absolute;
    width: 427px;
    height: 244px;
    background: var(--card);
    border-radius: 22px;
    box-shadow: 0 4px 10px rgba(0,0,0,0.22), 0 1px 3px rgba(0,0,0,0.15);
  }
  .card--deron { left: 122px; top: 104px; }
  .card--marisa { left: 110px; top: 375px; }
  .card--lakendra { left: 110px; top: 634px; }
  .card--samir { left: 110px; top: 912px; }

  .portrait {
    position: absolute;
    left: 58px; top: 56px;
    width: 105px; height: 132px;
    border: 1.5px solid var(--frame);
  }
  .portrait--deron { background: linear-gradient(160deg, #2b2c31 0%, #23283a 55%, #1d2438 100%); }
  .portrait--marisa { background: linear-gradient(160deg, #8a7a6a 0%, #5e4a3a 50%, #5d6040 100%); }
  .portrait--lakendra { background: linear-gradient(160deg, #f2efea 0%, #e6cdb8 55%, #dcb394 100%); }
  .portrait--samir { background: linear-gradient(160deg, #e4e1dd 0%, #bdb7b0 55%, #8f9586 100%); }

  .divider {
    position: absolute;
    left: 185px; top: 56px;
    width: 1px; height: 128px;
    background: var(--rule);
  }
  .details {
    position: absolute;
    left: 200px; top: 58px;
    width: 220px;
  }
  .name {
    font-weight: 700;
    font-size: 17px;
    line-height: 20px;
    margin-left: 4px;
    letter-spacing: -0.1px;
  }
  .title {
    font-size: 12px;
    line-height: 15px;
    margin-left: 2px;
    margin-top: 3px;
    color: var(--ink-soft);
  }
  .contact { list-style: none; margin-top: 7px; }
  .contact li {
    display: flex;
    align-items: center;
    font-size: 12px;
    line-height: 17.5px;
    white-space: nowrap;
  }
  .contact svg { width: 13px; height: 11px; margin-right: 6px; flex: none; fill: var(--ink); }
  .credentials { font-size: 12px; line-height: 16.5px; margin-top: 4px; }
  .credentials p:last-child { margin-left: 1px; }
</style>
</head>
<body>

<svg width="0" height="0" style="position:absolute">
  <defs>
    <symbol id="icon-office" viewBox="0 0 26 20">
      <path d="M1 7c0-4 6-6 12-6s12 2 12 6v2h-6V6.5c-2-.8-10-.8-12 0V9H1z"/>
      <path d="M8 8h10l4 10H4z"/>
      <g fill="#fff"><rect x="10" y="11" width="1.6" height="1.6"/><rect x="12.2" y="11" width="1.6" height="1.6"/><rect x="14.4" y="11" width="1.6" height="1.6"/><rect x="10" y="13.4" width="1.6" height="1.6"/><rect x="12.2" y="13.4" width="1.6" height="1.6"/><rect x="14.4" y="13.4" width="1.6" height="1.6"/></g>
    </symbol>
    <symbol id="icon-mobile" viewBox="0 0 22 20">
      <path d="M5 1l3.5 4-2 2.5c1 2.5 3.5 5 6 6l2.5-2 4 3.5-2.5 3.5C10 18 2 10 1.5 3.5z"/>
      <path d="M12 1.5a7 7 0 0 1 7 7" fill="none" stroke="#333437" stroke-width="1.6"/>
      <path d="M12 5a3.5 3.5 0 0 1 3.5 3.5" fill="none" stroke="#333437" stroke-width="1.6"/>
    </symbol>
    <symbol id="icon-mail" viewBox="0 0 24 18">
      <path d="M1 2h22v14H1z"/>
      <path d="M2 3l10 8 10-8" fill="none" stroke="#fff" stroke-width="1.8"/>
    </symbol>
  </defs>
</svg>

<article class="card card--deron">
  <div class="portrait portrait--deron" role="img" aria-label="Portrait photo of Deron Plummer"></div>
  <div class="divider"></div>
  <div class="details">
    <h2 class="name">Deron Plummer</h2>
    <p class="title">Mortgage Originator</p>
    <ul class="contact">
      <li><svg><use href="#icon-office"/></svg>(800) 555-0142 x66</li>
      <li><svg><use href="#icon-mobile"/></svg>(404) 555-0163</li>
      <li><svg><use href="#icon-mail"/></svg>dplummer@brightgatehomes.example</li>
    </ul>
    <div class="credentials"><p>NMLS 5917360</p><p>Licensed MD</p></div>
  </div>
</article>

<article class="card card--marisa">
  <div class="portrait portrait--marisa" role="img" aria-label="Portrait photo of Marisa Okonduye"></div>
  <div class="divider"></div>
  <div class="details">
    <h2 class="name">Marisa Okonduye</h2>
    <p class="title">Mortgage Originator</p>
    <ul class="contact">
      <li><svg><use href="#icon-office"/></svg>(800) 555-0142 x65</li>
      <li><svg><use href="#icon-mobile"/></svg>(240) 555-0187</li>
      <li><svg><use href="#icon-mail"/></svg>mokonduye@brightgatehomes.example</li>
    </ul>
    <div class="credentials"><p>NMLS 5830472</p><p>Licensed MD</p></div>
  </div>
</article>

<article class="card card--lakendra">
  <div class="portrait portrait--lakendra" role="img" aria-label="Portrait photo of Lakendra Burton"></div>
  <div class="divider"></div>
  <div class="details">
    <h2 class="name">Lakendra Burton</h2>
    <p class="title">Mortgage Originator</p>
    <ul class="contact">
      <li><svg><use href="#icon-office"/></svg>(800) 555-0142 x67</li>
      <li><svg><use href="#icon-mobile"/></svg>(443) 555-0129</li>
      <li><svg><use href="#icon-mail"/></svg>burtonlakendra@mailbox.example</li>
    </ul>
    <div class="credentials"><p>NMLS 5372619</p><p>Licensed MD</p></div>
  </div>
</article>

<article class="card card--samir">
  <div class="portrait portrait--samir" role="img" aria-label="Portrait photo of Samir Qudwaheli"></div>
  <div class="divider"></div>
  <div class="details">
    <h2 class="name">Samir Qudwaheli</h2>
    <p class="title">Mortgage Originator</p>
    <ul class="contact">
      <li><svg><use href="#icon-office"/></svg>(800) 555-0142 x32</li>
      <li><svg><use href="#icon-mobile"/></svg>(571) 555-0176</li>
      <li><svg><use href="#icon-mail"/></svg>squdwaheli@brightgatehomes.example</li>
    </ul>
    <div class="credentials"><p>NMLS 4068259</p><p>Licensed MD</p></div>
  </div>
</article>

</body>
</html>
```